My name is Tomas Verenda, and I have done business with your company several times. I need a business card to represent my business, I own a company by the name of BELOMI Suntan Lotion & Sunscreen.
My requirements are as follow: My company logo in the brightest gold possible, on a black, grainy (sandy) background, with shading around the each element. With the company name in gold, a stylized coconut trees, and some type of wave graphic in gold. "A product of the USA, Staten Island, NY"
"For comments, suggestion, or ordering please contact us at:
belomi42@nexamail.test"

"BELOMI™ Tanning Lotion & Sunscreen―Crafted with Care"

Belomi Tanning Lotion & Sunscreen is the most extraordinary and innovative sun tanning product to emerge in several generations. The constituents of this product are formidable substances that protect the skin against the aftermath of sun exposure−before you exposed yourself to the sun’s rays. The Aloe Vera in this product, along with other oils and cream, are specifically manufactured to lessen the symptoms of extended exposure to the sun. Belomi is designed to provide a Broad Spectrum Protection (50) that assist in the reduction of (UVA) and (UVB) radiation to create a magnificent sun-absorbing, long-lasting, deep dark bronzing experience.
Thank you,
Tomas Verenda
tomastverenda@postline.test

Target Market(s)

Sunscreen

Industry/Entity Type

Business

Contact Information for Business Card

BELOMI™ Tanning Lotion and Sunscreen
Crafted with Care

Belomi Tanning Lotion is the most extraordinary and innovative sun tanning product to emerge in several generations. The constituents of this product are formidable substances that protect the skin against the aftermath of sun exposure−before you exposed yourself to the sun’s rays. The Aloe Vera, in this product, along with other oils and cream, are specifically manufactured to lessen the symptoms of extended exposure to the sun. Belomi protects your skin from dehydration and treat your skin with the products we apply to ourselves after a sunburn−before the sun tanning process begins. Belomi is designed to provide a Broad Spectrum Protection (50) that assist in the reduction of (UVA) and (UVB) radiation to create a magnificent sun-absorbing, long-lasting, deep dark bronzing experience.

Colors
fece3e
acd136

Requirements
Must have
• Black Card Stock with grainy surface, Gold Logo, stylized Coconut Palm Tree, Company Name, email address, and NYC location.
• Modern Layout with Modern fonts and graphics

```html
<!DOCTYPE html>
<html lang="en">
<head>
<meta charset="utf-8">
<title>BELOMI Suntan Lotion – Business Card</title>
<link rel="stylesheet" href="https://fonts.googleapis.com/css2?family=Montserrat:wght@400;500;600;700&display=swap">
<style>
  :root {
    --backdrop: #2b2b2d;
    --card-black: #050505;
    --gold-bright: #fece3e;
    --gold-deep: #e8b320;
    --sand-pale: #f3df86;
    --brand-yellow: #f1d34a;
    --text-white: #ffffff;
    --text-dark: #1c1a12;
    --font-main: "Montserrat", Arial, sans-serif;
  }
  * { box-sizing: border-box; margin: 0; padding: 0; }
  html, body {
    width: 1200px;
    height: 900px;
    overflow: hidden;
    background: var(--backdrop);
    font-family: var(--font-main);
  }
  .canvas {
    position: relative;
    width: 1200px;
    height: 900px;
  }
  .card {
    position: absolute;
    width: 640px;
    height: 366px;
    border-radius: 22px;
    overflow: hidden;
    background: var(--card-black);
    box-shadow: 0 14px 30px rgba(0,0,0,0.45);
  }
  .card--front { left: 280px; top: 50px; }
  .card--back  { left: 280px; top: 474px; }

  /* Front face */
  .front-brand {
    position: absolute;
    left: 0; right: 0; top: 62px;
    display: flex;
    flex-direction: column;
    align-items: center;
  }
  .brand-disc {
    width: 96px; height: 96px;
    border-radius: 50%;
    background: var(--gold-deep);
    margin-bottom: 14px;
  }
  .brand-name {
    color: var(--text-white);
    font-weight: 600;
    font-size: 58px;
    letter-spacing: 2px;
    line-height: 1;
  }
  .brand-sub {
    color: var(--text-white);
    font-weight: 600;
    font-size: 25px;
    letter-spacing: 1px;
    margin-top: 4px;
  }
  .front-web {
    position: absolute;
    left: 0; right: 0; bottom: 38px;
    text-align: center;
    color: var(--text-white);
    font-size: 15px;
    font-weight: 500;
  }
  .front-web strong { color: var(--brand-yellow); font-weight: 700; }

  /* Back face */
  .back-swoosh { position: absolute; inset: 0; width: 640px; height: 366px; }
  .back-brand {
    position: absolute;
    left: 36px; top: 70px;
  }
  .back-brand .brand-name { font-size: 54px; }
  .back-brand .brand-sub { font-size: 23px; margin-left: 40px; }
  .back-disc {
    position: absolute;
    right: 92px; top: 30px;
    width: 118px; height: 118px;
    border-radius: 50%;
    background: var(--gold-deep);
  }
  .person {
    position: absolute;
    left: 56px; top: 196px;
    color: var(--text-white);
  }
  .person-name {
    color: var(--brand-yellow);
    font-weight: 600;
    font-size: 21px;
  }
  .person-role { font-size: 14px; margin-top: 2px; }
  .person-address { font-size: 15px; line-height: 1.35; margin-top: 12px; }

  .contact-list {
    position: absolute;
    right: 20px; top: 178px;
    list-style: none;
    text-align: right;
    color: var(--text-dark);
    font-size: 14px;
    line-height: 1.55;
  }
  .contact-list li { display: flex; align-items: center; justify-content: flex-end; gap: 8px; }
  .contact-list strong { font-weight: 700; }
  .contact-icon { width: 11px; height: 11px; flex: none; }
</style>
</head>
<body>
<main class="canvas">

  <section class="card card--front" aria-label="Card front">
    <div class="front-brand">
      <div class="brand-disc"></div>
      <div class="brand-name">BELOMI</div>
      <div class="brand-sub">SUNTAN LOTION</div>
    </div>
    <p class="front-web">www.<strong>belomisuntanlotion</strong>.test</p>
  </section>

  <section class="card card--back" aria-label="Card back">
    <svg class="back-swoosh" viewBox="0 0 640 366" aria-hidden="true">
      <rect width="640" height="366" fill="var(--card-black)"/>
      <path d="M448,0 C420,60 410,150 360,225 C300,310 170,340 0,336 L0,366 L640,366 L640,0 Z" fill="var(--gold-bright)"/>
      <path d="M456,0 C430,60 420,155 372,230 C315,316 180,348 0,346" fill="none" stroke="var(--card-black)" stroke-width="3"/>
      <path d="M470,0 C448,60 440,160 392,236 C335,322 200,354 0,356 L0,366 L640,366 L640,0 Z" fill="var(--sand-pale)"/>
    </svg>
    <div class="back-brand">
      <div class="brand-name">BELOMI</div>
      <div class="brand-sub">SUNTAN LOTION</div>
    </div>
    <div class="back-disc"></div>
    <div class="person">
      <p class="person-name">Marcus Ellery</p>
      <p class="person-role">Director</p>
      <p class="person-address">48 Harbor View Lane<br>Staten Island, NY 10301</p>
    </div>
    <ul class="contact-list">
      <li>+1 718 555-0142
        <svg class="contact-icon" viewBox="0 0 12 12"><path d="M2.5,1 L4.5,1 L5.3,3.6 L4,4.6 C4.7,6 6,7.3 7.4,8 L8.4,6.7 L11,7.5 L11,9.5 C11,10.4 10.3,11 9.5,11 C5,11 1,7 1,2.5 C1,1.7 1.6,1 2.5,1 Z" fill="#2f7a3a"/></svg>
      </li>
      <li>belomi42@nexamail.test
        <svg class="contact-icon" viewBox="0 0 12 12"><rect x="1" y="2.5" width="10" height="7" rx="1" fill="none" stroke="#2f7a3a" stroke-width="1.3"/><path d="M1.5,3 L6,6.5 L10.5,3" fill="none" stroke="#2f7a3a" stroke-width="1.2"/></svg>
      </li>
      <li>www.<strong>belomisuntanlotion</strong>.test
        <svg class="contact-icon" viewBox="0 0 12 12"><circle cx="6" cy="6" r="5" fill="none" stroke="#2f7a3a" stroke-width="1.2"/><path d="M1,6 L11,6 M6,1 C3.5,4 3.5,8 6,11 M6,1 C8.5,4 8.5,8 6,11" fill="none" stroke="#2f7a3a" stroke-width="1"/></svg>
      </li>
    </ul>
  </section>

</main>
</body>
</html>
```